Re Design of Business Cards

We a Technology & Telecommunications company, we supply computer repairs suppy and services to home and business's, we also a Telecommunications company as well and that we supply Internet, Mobile Voice and Data and Voice Lines to home and business as well we want to get our business cards re designed that stand out but also state what we can do and that we also come to you, there is 4 of us in the business so we all need same business card design but just different names and phone numbers on all.
Ive upload our Logo as well. and current looking business cards.

Our current business cards does not make me excited and or stand out, to dark and does not say what we do, we leave our business cards in letter boxes some times and in receptions of villages for retiress so the reception can hand out, few times now there asked what do you do, so thinking one side is our contact details and other is our services

I think I like to also put our address onto it as well, very simple as its also my home address but it be good to have it on there

48 Tindall Cres - Corvan Heights NSW 2318

We should also have our business rego number which is a ABN

ABN: 92 417 306 845

this way we all covered and we look very Professional

We would like to make some Points, 1st of All we just found out we do not need out ABN on our Business Cards so we can Remove that please

we would like the address for the business to be on cards as well,

On the flip side of the Business Cards we would like to list some of our services as below

High-Speed Internet for Home & Business
Managed IT Services & Support
Network Setup & Optimization
VoIP & Mobile Voice Solutions
Wi-Fi Installation & Troubleshooting
Smart Home & Office Technology
Data Backup & Cybersecurity
Onsite Home and Or Business

```html
<!DOCTYPE html>
<html lang="en">
<head>
<meta charset="utf-8">
<title>Norvale Business Cards</title>
<link href="https://fonts.googleapis.com/css2?family=Lexend:wght@300;400;500;600&display=swap" rel="stylesheet">
<style>
  :root {
    --bg: #e9e8e6;
    --card-front: #f8f8f8;
    --card-back: #c8e3ec;
    --navy: #0d2f57;
    --teal: #13a9ad;
    --ink: #22344c;
  }
  * { margin: 0; padding: 0; box-sizing: border-box; }
  html, body {
    width: 1200px; height: 1199px; overflow: hidden;
    background: var(--bg);
    font-family: "Lexend", sans-serif;
    color: var(--ink);
  }
  .card { position: absolute; border-radius: 14px; overflow: hidden; }
  .card-front {
    left: 182px; top: 318px; width: 527px; height: 295px;
    background: var(--card-front); z-index: 2;
  }
  .card-back {
    left: 516px; top: 566px; width: 497px; height: 299px;
    background: var(--card-back); z-index: 1;
  }
  .brand { position: absolute; left: 36px; top: 23px; display: flex; align-items: center; gap: 12px; }
  .brand-dot { width: 70px; height: 70px; border-radius: 50%; background: var(--navy); }
  .brand-name { font-size: 26px; font-weight: 500; letter-spacing: 4px; color: var(--navy); }
  .person-name { position: absolute; left: 45px; top: 112px; font-size: 29px; font-weight: 600; color: var(--navy); }
  .person-role { position: absolute; left: 45px; top: 148px; font-size: 19px; font-weight: 400; color: var(--ink); }
  .rule { position: absolute; left: 44px; top: 187px; width: 439px; height: 2px; background: var(--teal); }
  .contact { position: absolute; font-size: 18.5px; font-weight: 400; color: var(--ink); display: flex; align-items: center; gap: 8px; white-space: nowrap; }
  .contact svg { width: 16px; height: 16px; fill: var(--teal); flex: none; }
  .services-title { position: absolute; left: 206px; top: 22px; font-size: 26px; font-weight: 600; color: var(--navy); }
  .services-rule { position: absolute; left: 204px; top: 58px; right: 0; height: 2px; background: var(--navy); }
  .service { position: absolute; display: flex; gap: 8px; font-size: 15px; font-weight: 400; line-height: 19px; color: var(--navy); white-space: nowrap; }
  .service svg { width: 24px; height: 24px; flex: none; fill: none; stroke: var(--navy); stroke-width: 1.5; margin-top: 3px; }
</style>
</head>
<body>

<section class="card card-front">
  <div class="brand">
    <div class="brand-dot"></div>
    <span class="brand-name">NORVALE</span>
  </div>
  <h1 class="person-name">Sam Corbett</h1>
  <p class="person-role">Sales Consultant</p>
  <div class="rule"></div>

  <p class="contact" style="left:46px;top:202px;">
    <svg viewBox="0 0 24 24"><path d="M6.6 10.8a15.1 15.1 0 0 0 6.6 6.6l2.2-2.2a1 1 0 0 1 1-.25 11.4 11.4 0 0 0 3.6.57 1 1 0 0 1 1 1V20a1 1 0 0 1-1 1A17 17 0 0 1 3 4a1 1 0 0 1 1-1h3.5a1 1 0 0 1 1 1c0 1.250.2 2.450.57 3.57a1 1 0 0 1-.25 1z"/></svg>
    0400 555 123
  </p>
  <p class="contact" style="left:274px;top:202px;">1800 555 019</p>
  <p class="contact" style="left:46px;top:230px;">
    <svg viewBox="0 0 24 24"><path d="M2 5h20v14H2z M2 5l10 7 10-7" /></svg>
    sam@norvale.com.au
  </p>
  <p class="contact" style="left:274px;top:230px;">norvale.com.au</p>
  <p class="contact" style="left:46px;top:261px;">
    <svg viewBox="0 0 24 24"><path d="M12 2a7 7 0 0 0-7 7c0 5 7 13 7 13s7-8 7-13a7 7 0 0 0-7-7zm0 9.5A2.5 2.5 0 1 1 12 6.5a2.5 2.5 0 0 1 0 5z"/></svg>
    48 Tindall Cres - Corvan Heights NSW 2318
  </p>
</section>

<section class="card card-back">
  <h2 class="services-title">Our Services</h2>
  <div class="services-rule"></div>

  <div class="service" style="left:30px;top:78px;">
    <svg viewBox="0 0 24 24"><circle cx="12" cy="12" r="10"/><ellipse cx="12" cy="12" rx="4.5" ry="10"/><path d="M2 12h20M4 7h16M4 17h16"/></svg>
    <span>High-Speed Internet<br>for Home &amp; Business</span>
  </div>
  <div class="service" style="left:30px;top:129px;">
    <svg viewBox="0 0 24 24"><rect x="4" y="5" width="16" height="11"/><path d="M1.5 19h21"/></svg>
    <span>Managed IT Services<br>&amp; Support</span>
  </div>
  <div class="service" style="left:30px;top:180px;">
    <svg viewBox="0 0 24 24"><circle cx="10" cy="10" r="8"/><ellipse cx="10" cy="10" rx="3.5" ry="8"/><path d="M2 10h16"/><circle cx="18" cy="18" r="3"/></svg>
    <span>Network Setup<br>&amp; Optimization</span>
  </div>
  <div class="service" style="left:30px;top:231px;">
    <svg viewBox="0 0 24 24"><path d="M6.6 10.8a15.1 15.1 0 0 0 6.6 6.6l2.2-2.2a1 1 0 0 1 1-.25 11.4 11.4 0 0 0 3.6.57 1 1 0 0 1 1 1V20a1 1 0 0 1-1 1A17 17 0 0 1 3 4a1 1 0 0 1 1-1h3.5a1 1 0 0 1 1 1c0 1.25.2 2.45.57 3.57a1 1 0 0 1-.25 1z"/></svg>
    <span>VoIP &amp; Mobile Voice<br>Solutions</span>
  </div>
  <div class="service" style="left:262px;top:78px;">
    <svg viewBox="0 0 24 24"><path d="M3 9a13 13 0 0 1 18 0M6 12.5a8.5 8.5 0 0 1 12 0M9 16a4 4 0 0 1 6 0"/><circle cx="12" cy="19.5" r="1.2"/></svg>
    <span>Wi-Fi Installation<br>&amp; Troubleshooting</span>
  </div>
  <div class="service" style="left:262px;top:129px;">
    <svg viewBox="0 0 24 24"><path d="M3 11l9-8 9 8M5 9.5V21h14V9.5M10 21v-6h4v6"/></svg>
    <span>Smart Home<br>&amp; Office Technology</span>
  </div>
  <div class="service" style="left:262px;top:180px;">
    <svg viewBox="0 0 24 24"><path d="M12 2l8 3v6c0 5-3.5 9-8 11-4.5-2-8-6-8-11V5z"/><path d="M8.5 12l2.5 2.5 4.5-5"/></svg>
    <span>Data Backup<br>&amp; Cybersecurity</span>
  </div>
  <div class="service" style="left:262px;top:231px;">
    <svg viewBox="0 0 24 24"><rect x="3" y="6" width="18" height="12"/><path d="M1 21h22M12 9v6M9 12h6"/></svg>
    <span>Onsite Home<br>&amp; Business Support</span>
  </div>
</section>

</body>
</html>
```